Web Site Design for a Finance (lending) Company

We are opening a new subsidiary that focuses on lending money in the real estate industry. We need a web site designed to represent the business.

The business is lending money to real estate investors. A typical client/borrower will be looking to borrow money to buy a house, renovate it and then sell it at a profit, all within 12 months or less.

Company name is Brevand Finance. Our logo is attached.

Attached is a general outline for the web site. We're working on writing more text for each page but this should give you enough to get started with some ideas.

Competitor web site that I like a lot (as an example): https://quorvelfunding.com/. Many of the general items on this site match what we will need (description of loan programs, FAQ)

Target Market(s)

Real estate investors (generally individuals or small companies with just a few people) who are buying homes, renovating them and then selling them at a profit.

Industry/Entity Type

Finance

Coding

Coded - Design and coding required

Number of Pages Required

5+ page

Colors

Designer to choose colors to be used in the design.

Requirements
Must have
• Minimalist design. Clean lines without too much clutter. Some stock photography is ok but the photos should not be distracting. They should almost fade in to the background so that user can focus on the key information about what our company does instead. We are a finance company, not a design company, so the information about our products will be more interesting to site visitors than the art.
• Some minimalist examples from Snapboard:
• https://www.snapboard-example.com/explore/minimalist-web-design/
Nice to have
• If you search in seekly for "hard money lenders" you will find many examples of web sites from our competition. I have provided a link above to competitor web site that I like a lot.
• I have attached our logo in EPS format. Logo is green. Web site doesn't have to be green but it should be of a color that will work well with the logo.

```html
<!DOCTYPE html>
<html lang="en">
<head>
<meta charset="utf-8">
<title>Brevand Finance — Local Real Estate Experts</title>
<link rel="stylesheet" href="https://fonts.googleapis.com/css2?family=PT+Sans:wght@400;700&family=Alegreya:ital,wght@0,400;0,700;1,400;1,700&family=Lato:wght@400;700&display=swap">
<style>
:root{
  --ink:#2b2927;
  --ink-soft:#55514d;
  --accent:#a5693b;
  --brand:#3d7a55;
  --paper:#ffffff;
  --mist:#eeeeec;
  --line:#c9c5c0;
  --dark:#2f2c2a;
}
*{box-sizing:border-box;margin:0;padding:0}
html,body{width:1200px;height:4700px;overflow:hidden}
body{position:relative;background:var(--paper);color:var(--ink);font-family:"Lato",sans-serif}
.abs{position:absolute}
.sans{font-family:"PT Sans",sans-serif}
.serif{font-family:"Alegreya",serif}
.btn{position:absolute;display:flex;align-items:center;justify-content:center;font:700 13px/1 "Lato",sans-serif;letter-spacing:1.5px;text-transform:uppercase;border:2px solid var(--accent);color:var(--ink);background:#fff;border-radius:3px}
.btn.dark{background:var(--ink);border-color:var(--ink);color:#fff}
.photo{position:absolute}

/* header */
.brand{left:28px;top:46px;display:flex;align-items:center;gap:12px}
.brand-mark{width:30px;height:30px;background:var(--brand)}
.brand-name{font:700 22px/1.05 "PT Sans",sans-serif;color:var(--ink)}
.brand-name span{display:block;font-weight:400;color:var(--ink-soft)}
.topbar{right:50px;top:34px;font-size:12px;color:var(--ink-soft);display:flex;gap:20px}
.nav{right:120px;top:92px;display:flex;gap:34px;font-size:12px;text-transform:uppercase;letter-spacing:1px;color:var(--ink-soft)}
.nav .on{color:var(--accent)}
.search{right:46px;top:80px;width:36px;height:34px;border:2px solid var(--accent);border-radius:3px}

/* hero */
.hero-title{left:0;width:1200px;top:160px;text-align:center;font:700 46px/1 "PT Sans",sans-serif;letter-spacing:2px}
.hero-sub{left:0;width:1200px;top:224px;text-align:center;font:italic 24px/1 "Alegreya",serif;color:var(--ink-soft)}
.hero-bg{left:0;top:285px;width:1200px;height:790px;background:linear-gradient(180deg,#fff 0%,#e7e5e1 30%,#cfccc6 60%,#e2e0dc 85%,#fff 100%)}
.hero-drawing{left:335px;top:400px;width:535px;height:340px;background:linear-gradient(180deg,rgba(255,255,255,.75),rgba(255,255,255,.55))}
.card{top:750px;width:455px;height:245px;background:var(--dark);color:#fff;padding:24px 34px}
.card-icon{position:absolute;left:50%;transform:translateX(-50%);top:28px;width:90px;height:50px;border:1px solid rgba(255,255,255,.35)}
.card h3{position:absolute;left:0;width:100%;top:88px;text-align:center;font:700 26px/1 "PT Sans",sans-serif;letter-spacing:1px}
.card-rule{position:absolute;left:60px;right:60px;top:126px;border-top:1px solid rgba(255,255,255,.5)}
.card p{position:absolute;left:40px;right:40px;top:140px;text-align:center;font-size:12.5px;line-height:1.5;color:#ddd}
.card .more{position:absolute;left:34px;bottom:24px;font-size:10px;letter-spacing:1px}
.card .ghost{position:absolute;right:28px;bottom:16px;font:italic 28px/1 "Alegreya",serif;color:rgba(255,255,255,.2)}

/* intro */
.intro{left:120px;width:960px;top:1118px;font:italic 24px/1.6 "Alegreya",serif;color:var(--ink)}
.intro b{font-size:40px;font-weight:400}
.intro p+p{margin-top:26px}

/* why */
.big{font:700 86px/1.2 "PT Sans",sans-serif;letter-spacing:22px}
.checks{left:148px;top:1755px;list-style:none;font:15px/1 "Alegreya",serif;text-transform:uppercase;letter-spacing:1px;color:var(--ink-soft)}
.checks li{display:flex;align-items:center;gap:12px;height:34px}

/* loans */
.tabs{left:610px;top:2205px;display:flex;gap:22px;font:16px/1 "Alegreya",serif;text-transform:uppercase;letter-spacing:1px}
.tabs .on{color:var(--accent)}
.loan-text{left:610px;width:470px;top:2262px;font:700 12.5px/1.62 "Lato",sans-serif;color:var(--ink)}

/* team */
.team-text{left:120px;width:460px;top:2905px;font-size:12.5px;line-height:1.6;color:var(--ink-soft)}
.member{left:120px;top:3032px;font-size:12px;line-height:1.4}
.member b{display:block}
.dots{left:298px;top:3160px;display:flex;gap:12px}
.dots i{width:14px;height:14px;border:2px solid var(--line);border-radius:50%}
.dots i:first-child{background:var(--line)}

/* testimonials */
.testi-bg{left:0;top:3270px;width:1200px;height:400px;background:linear-gradient(180deg,#fff,#e9e8e5 40%,#e4e2df 70%,#fff)}
.testi-title{left:0;width:1200px;top:3305px;text-align:center;font:700 34px/1 "PT Sans",sans-serif;letter-spacing:9px}
.testi-text{left:320px;width:560px;top:3390px;text-align:center;font:700 12.5px/1.6 "Lato",sans-serif}
.arrow{width:20px;height:24px;background:var(--ink);color:#fff;display:flex;align-items:center;justify-content:center;font-size:12px}
.avatar{left:546px;top:3476px;width:80px;height:80px;border-radius:50%;border:3px solid var(--accent);background:linear-gradient(180deg,#d8c9b5,#7c6a58)}
.quoter{left:634px;top:3500px;font-size:11px;line-height:1.35}

/* partners */
.partners{left:120px;width:960px;top:3680px;height:70px;display:flex;justify-content:space-between;align-items:center;font:700 22px/1 "PT Sans",sans-serif;color:#8a8784}
.partners span{display:flex;align-items:center;gap:10px}
.partners i{width:22px;height:22px;border-radius:50%;background:#a9a6a2;display:inline-block}

/* newsletter */
.news{left:0;top:3803px;width:1200px;height:135px;background:var(--dark);color:#fff}
.news h4{position:absolute;left:75px;top:52px;font:700 26px/1 "Alegreya",serif}
.news .field{position:absolute;left:710px;top:47px;width:265px;height:42px;border:1px solid #bbb;background:#fff;padding:12px;font-size:12px;color:#999}
.news .go{position:absolute;left:988px;top:47px;width:125px;height:42px;background:#8a8682;color:#fff;font-size:12px;letter-spacing:1.5px;display:flex;align-items:center;justify-content:center}

/* contact */
.qc-title{left:0;width:1200px;top:3996px;text-align:center;font:700 36px/1 "PT Sans",sans-serif;letter-spacing:9px}
.qc-rule{left:520px;width:160px;top:4055px;border-top:1px solid var(--accent)}
.qc-sub{left:0;width:1200px;top:4070px;text-align:center;font:italic 24px/1 "Alegreya",serif;color:var(--accent)}
.input{position:absolute;border:2px solid var(--ink-soft);border-radius:2px;font:italic 14px/1 "Alegreya",serif;color:#666;padding:8px 12px}
.submit{left:780px;top:4400px;width:106px;height:42px;background:var(--dark);color:#fff;font:700 12px/1 "Lato",sans-serif;letter-spacing:2px;display:flex;align-items:center;justify-content:center;border-radius:3px}

/* footer */
.foot-brand{left:418px;top:4500px;display:flex;align-items:center;gap:12px}
.foot-div{left:660px;top:4500px;height:60px;border-left:1px solid var(--line)}
.foot-contact{left:680px;top:4508px;font:700 13px/2 "Lato",sans-serif}
.social{left:566px;top:4590px;display:flex;gap:14px}
.social i{width:20px;height:20px;background:var(--ink-soft);border-radius:2px}
.copy{left:0;width:1200px;top:4640px;text-align:center;font-size:12px;color:var(--ink-soft)}
</style>
</head>
<body>

<header>
  <div class="abs brand"><span class="brand-mark"></span><div class="brand-name">Brevand<span>Finance</span></div></div>
  <div class="abs topbar"><span>&#9742; (555) 014-2270</span><span>&#9679; Login / Sign Up</span></div>
  <nav class="abs nav"><span class="on">Home</span><span>About Us</span><span>Loans</span><span>Resources</span><span>Contact Us</span><span>Apply Now</span></nav>
  <div class="abs search"><svg width="32" height="30" viewBox="0 0 32 30"><circle cx="14" cy="13" r="6" fill="none" stroke="#a5693b" stroke-width="2"/><line x1="18.5" y1="17.5" x2="23" y2="22" stroke="#a5693b" stroke-width="2"/></svg></div>
</header>

<section class="hero">
  <div class="abs hero-bg" role="img" aria-label="Softly faded photograph of a suburban street of family houses"></div>
  <h1 class="abs hero-title">LOCAL REAL ESTATE EXPERTS</h1>
  <p class="abs hero-sub">Lending to Local Real Estate Investors</p>
  <a class="btn" style="left:442px;top:323px;width:150px;height:48px">Learn More</a>
  <a class="btn dark" style="left:608px;top:323px;width:150px;height:48px">Apply Now</a>
  <svg class="abs" style="left:330px;top:335px" width="540" height="410" viewBox="0 0 540 410" fill="none" stroke="#3a3734" stroke-width="2">
    <polyline points="5,0 5,240 190,240"/>
    <polyline points="535,0 535,240 350,240"/>
    <line x1="190" y1="240" x2="190" y2="410"/>
  </svg>
  <div class="abs hero-drawing" role="img" aria-label="Line drawing of a cut-away house showing furnished rooms" style="left:430px;top:420px;width:340px;height:315px"></div>

  <article class="abs card" style="left:125px">
    <div class="card-icon" role="img" aria-label="Small outline house icon"></div>
    <h3>FIX AND FLIP</h3><div class="card-rule"></div>
    <p>Short term funding to buy, renovate and resell homes. Fast approval and simple terms for local investors.</p>
    <span class="more">LEARN MORE &rsaquo;</span><span class="ghost">0% Interest</span>
  </article>
  <article class="abs card" style="left:625px">
    <div class="card-icon" role="img" aria-label="Small outline office building icon"></div>
    <h3>COMMERCIAL</h3><div class="card-rule"></div>
    <p>Flexible loans for commercial property. Clear rates and quick closing for growing investment portfolios.</p>
    <span class="more">LEARN MORE &rsaquo;</span><span class="ghost">0 Down Payment</span>
  </article>
</section>

<section class="abs intro">
  <p><b>Brevand</b> Finance is a local business with local knowledge and strong industry relationships. A partner with a wide network who offers value added services</p>
  <p>Brevand has an established pool of experienced investors available for your real estate investment needs</p>
</section>
<a class="btn" style="left:544px;top:1393px;width:112px;height:40px;font-size:11px">Learn More</a>

<section class="why">
  <h2 class="abs big" style="left:122px;top:1490px">WHY<br>BREVAND</h2>
  <ul class="abs checks">
    <li><svg width="16" height="14"><path d="M1 7l5 5 9-11" fill="none" stroke="#a5693b" stroke-width="2"/></svg>Experts</li>
    <li><svg width="16" height="14"><path d="M1 7l5 5 9-11" fill="none" stroke="#a5693b" stroke-width="2"/></svg>Fast Approval</li>
    <li><svg width="16" height="14"><path d="M1 7l5 5 9-11" fill="none" stroke="#a5693b" stroke-width="2"/></svg>Professional</li>
    <li><svg width="16" height="14"><path d="M1 7l5 5 9-11" fill="none" stroke="#a5693b" stroke-width="2"/></svg>A Partner</li>
    <li><svg width="16" height="14"><path d="M1 7l5 5 9-11" fill="none" stroke="#a5693b" stroke-width="2"/></svg>Selective</li>
    <li><svg width="16" height="14"><path d="M1 7l5 5 9-11" fill="none" stroke="#a5693b" stroke-width="2"/></svg>Competitive Rates and Fees</li>
  </ul>
  <a class="btn" style="left:494px;top:1975px;width:112px;height:42px;font-size:11px">Learn More</a>
  <div class="photo" role="img" aria-label="Photograph of a modern white house with wood-clad upper storey" style="left:686px;top:1515px;width:354px;height:522px;background:linear-gradient(180deg,#c9c8c4 0%,#f2f1ee 35%,#6b6258 70%,#5f6a4c 100%)"></div>
  <div class="photo" role="img" aria-label="Faded interior photograph with dark armchair" style="left:1040px;top:1688px;width:160px;height:268px;background:linear-gradient(180deg,#e6e4e0,#9d958c 70%,#4a4541)"></div>
</section>

<section class="loans">
  <div class="photo" role="img" aria-label="Faded photograph of a house porch" style="left:0;top:2190px;width:160px;height:345px;background:linear-gradient(90deg,#fff,#dcd9d4)"></div>
  <div class="photo" role="img" aria-label="Photograph of a grey clapboard house with a red front door" style="left:158px;top:2092px;width:358px;height:523px;background:linear-gradient(180deg,#eeeeec 0%,#3f4a45 28%,#c8c9c6 50%,#b5b5b0 80%,#7c8a63 100%)"></div>
  <div class="abs tabs"><span class="on">Fix and Flip Loan</span><span style="color:#bbb">|</span><span>Commercial Loan</span></div>
  <p class="abs loan-text">A fix and flip loan is designed for investors who buy a home, improve it and sell it within twelve months or less. We fund the purchase and part of the renovation costs, with terms built around a short project timeline. Approval is fast and based on the value of the property after repairs, not only on personal income. Our local team reviews each deal with care, visits the site and stays in touch through every stage of the work so you can focus on the project and close on time.</p>
  <a class="btn" style="left:610px;top:2470px;width:106px;height:42px;font-size:11px">Learn More</a>
</section>

<section class="team">
  <h2 class="abs big" style="left:122px;top:2670px">OUR<br>TEAM</h2>
  <p class="abs team-text">Our lending team brings years of local market knowledge and real experience with renovation projects. We work closely with each investor, answer questions quickly and help shape every loan around the plan for the property and its sale.</p>
  <div class="abs member"><b>TOMAS REYL</b>President</div>
  <div class="abs dots"><i></i><i></i><i></i><i></i><i></i></div>
  <div class="photo" role="img" aria-label="Faded photograph of a group at a meeting table" style="left:1035px;top:2850px;width:165px;height:280px;background:linear-gradient(90deg,#bcb8b2,#e9e7e4)"></div>
  <div class="photo" role="img" aria-label="Portrait photograph of a team member in a suit" style="left:686px;top:2677px;width:352px;height:525px;background:linear-gradient(180deg,#e9e8e6 0%,#d9d6d2 40%,#3a3d44 70%,#23262c 100%)"></div>
</section>

<section class="testimonials">
  <div class="abs testi-bg" role="img" aria-label="Faded photograph of a row of houses"></div>
  <h2 class="abs testi-title">TESTIMONIALS</h2>
  <p class="abs testi-text">Working with this team made our first flip simple. The loan closed quickly, the terms were clear and they answered every question along the way. We have already started our second project with them.</p>
  <span class="abs arrow" style="left:242px;top:3418px">&lsaquo;</span>
  <span class="abs arrow" style="left:932px;top:3418px">&rsaquo;</span>
  <div class="abs avatar" role="img" aria-label="Round portrait of the client"></div>
  <div class="abs quoter"><b>MAREK OLSEN</b><br>Investor</div>
</section>

<section>
  <span class="abs" style="left:32px;top:3700px;font-size:30px;color:#888">&lsaquo;</span>
  <span class="abs" style="left:1148px;top:3700px;font-size:30px;color:#888">&rsaquo;</span>
  <div class="abs partners">
    <span><i></i>Fernlow</span><span><i></i>Pellar Co</span><span><i></i>Harwick Build</span><span><i></i>Lintel Research</span><span><i></i>Quillay</span>
  </div>
</section>

<section class="abs news">
  <h4>Subscribe to our newsletter &amp; be in touch</h4>
  <div class="field">Email</div>
  <div class="go">SUBSCRIBE</div>
</section>

<section class="contact">
  <h2 class="abs qc-title">QUICK CONTACT</h2>
  <div class="abs qc-rule"></div>
  <p class="abs qc-sub">We reply within one business day</p>
  <div class="input" style="left:313px;top:4132px;width:276px;height:38px">Name...</div>
  <div class="input" style="left:608px;top:4132px;width:278px;height:38px">Email...</div>
  <div class="input" style="left:313px;top:4180px;width:276px;height:38px">Phone...</div>
  <div class="input" style="left:608px;top:4180px;width:278px;height:38px">Subject...</div>
  <div class="input" style="left:313px;top:4228px;width:573px;height:160px">Message...</div>
  <div class="abs submit">SUBMIT</div>
</section>

<footer>
  <div class="abs foot-brand"><span class="brand-mark"></span><div class="brand-name">Brevand<span>Finance</span></div></div>
  <div class="abs foot-div"></div>
  <div class="abs foot-contact">&#9742; (555) 014-2270<br>&#9993; hello@brevandfinance.com</div>
  <div class="abs social"><i></i><i></i><i></i></div>
  <p class="abs copy">Copyright &copy; Brevand Finance</p>
</footer>

</body>
</html>
```